Equipment Supplier Brochure Needed

We need a professional one-page, front-and-back brochure for Tovrix, an equipment and parts supplier serving peanut shelling and processing facilities across the Southeast. This brochure will be used as a leave-behind with plant managers and procurement teams, so it must look clean, modern, and visually strong.

Front of brochure:

Tovrix logo and strong branding

Brief headline/summary of what Tovrix does

Product category overview listed on the front (high-level, clean layout)

Flat Screens (slot, round, herringbone, square, Style 1 & Style 2)

Sheller Grates

Ripple Screens

Sheller Bars

Eccentric Bearing Housings

Eccentric Shafts

Rebuilt Machines

Ducts

Sprockets

Rubber Gum Balls

Fiberglass

Mellin Pike Reels

Elevator Buckets

Space for several product photos (we’ve uploaded images)

Clean industrial aesthetic

Back of brochure:

More detailed visual layout of products

Strong callout section showing companies we represent (logos included)

Optional short paragraph about Tovrix’s capabilities, history, or differentiators

Contact info section

Overall style:

Clean, modern, print-ready

Industrial yet polished

Balanced visual + text layout

Color palette aligned with Tovrix brand

Final files delivered as print-ready PDF (plus editable source file if available)

We’ve uploaded product imagery, partner logos, and reference materials. Please design multiple layout concepts if possible.

```html
<!DOCTYPE html>
<html lang="en">
<head>
<meta charset="utf-8">
<title>Tovrix – Replacement Parts for Peanut Processing Equipment</title>
<link href="https://fonts.googleapis.com/css2?family=Montserrat:wght@400;500;600;700;800;900&display=swap" rel="stylesheet">
<style>
  :root{
    --brand-blue:#1f4fa6;
    --brand-blue-dark:#173f8a;
    --brand-tan:#dcc6a0;
    --ink:#161616;
    --paper:#ffffff;
    --page-bg:#8c8c8c;
  }
  *{box-sizing:border-box;margin:0;padding:0}
  html,body{width:751px;height:1200px;overflow:hidden;background:var(--page-bg)}
  body{font-family:"Montserrat",sans-serif;color:var(--ink);position:relative}

  .sheet{position:absolute;left:166px;width:646px;height:908px;background:var(--paper);overflow:hidden;
    transform:scale(0.6475);transform-origin:0 0;box-shadow:0 4px 10px rgba(0,0,0,.35)}
  .sheet.front{top:8px}
  .sheet.back{top:604px}
  .abs{position:absolute}

  /* ---------- Front ---------- */
  .brand{left:35px;top:28px;font-weight:900;font-size:44px;letter-spacing:1px;color:var(--brand-blue);line-height:1}
  .hero-band{left:0;top:86px;width:646px;height:217px;
    background:linear-gradient(100deg,var(--brand-blue-dark) 0%,var(--brand-blue) 55%,#3b66b8 100%)}
  .hero-text{left:35px;top:110px;color:#fff}
  .hero-kicker{font-weight:500;font-size:15px;margin-bottom:6px}
  .hero-title{font-weight:800;font-size:27px;line-height:30px;text-transform:uppercase}
  .hero-title .accent{color:var(--brand-tan);font-size:31px}
  .hero-photo{left:318px;top:15px;width:301px;height:330px}

  .intro{left:35px;top:324px;width:578px;font-size:11.6px;line-height:16px}
  .intro .lead{font-weight:600}
  .intro .detail{font-weight:500;margin-top:6px;text-align:justify}

  .section-head{left:35px;width:581px;display:flex;align-items:center;font-weight:700;font-size:16.5px;line-height:1}
  .section-head::after{content:"";flex:1;height:1.5px;background:var(--brand-blue);margin-left:10px}
  .section-head.categories{top:447px}
  .section-head.products{top:628px}

  .category-band{left:0;top:474px;width:646px;height:136px;background:var(--brand-tan);display:flex}
  .category-col{list-style:none;padding-top:8px;font-weight:500;font-size:14.5px;line-height:21.5px}
  .category-col:nth-child(1){width:221px;padding-left:35px}
  .category-col:nth-child(2){width:212px;padding-left:30px;border-left:1.5px solid #fff}
  .category-col:nth-child(3){flex:1;padding-left:19px;border-left:1.5px solid #fff}
  .tick-list li{position:relative;padding-left:21px}
  .tick-list li::before{content:"";position:absolute;left:0;top:5.5px;width:11px;height:11px;border-radius:50%;background:var(--brand-blue)}
  .tick-list li::after{content:"";position:absolute;left:3.2px;top:8px;width:4.6px;height:2.6px;border-left:1.5px solid #fff;border-bottom:1.5px solid #fff;transform:rotate(-45deg)}
  .category-col li.wrap{line-height:16px;padding-top:3px}
  .category-col li.wrap::before{top:5.5px}
  .category-col li.wrap::after{top:8px}

  .product-row{left:34px;top:656px;width:583px;display:flex;justify-content:space-between}
  .product-tile{width:136px;height:142px;border:4px solid var(--brand-blue);border-radius:12px}
  .tile-screens{background:linear-gradient(160deg,#9a9a98,#d8d6d1 50%,#7c7b78)}
  .tile-housing{background:linear-gradient(150deg,#5e5d5a,#bdbab4 50%,#6f6c68)}
  .tile-shafts{background:linear-gradient(135deg,#a39c8f,#d9d4ca 50%,#8a8378)}
  .tile-reels{background:linear-gradient(180deg,#2c4f94,#9a9791 45%,#6d6964)}

  .footer{left:0;top:835px;width:646px;height:73px}
  .location{left:35px;top:856px;color:#fff;display:flex;align-items:center;gap:9px}
  .back .location{left:64px}
  .location-label{color:var(--brand-tan);font-weight:700;font-size:13px;line-height:15px}
  .location-address{font-weight:600;font-size:10.8px;line-height:14px}
  .contact{right:28px;top:837px;text-align:right}
  .contact-name{font-weight:700;font-size:13.5px;line-height:16px}
  .contact-email{font-weight:500;font-size:11.5px;line-height:15px;display:flex;align-items:center;justify-content:flex-end;gap:7px}
  .contact-phone{font-weight:700;font-size:16.5px;line-height:20px;display:flex;align-items:center;justify-content:flex-end;gap:7px;margin-top:13px}

  /* ---------- Back ---------- */
  .cap-band{left:0;top:0;width:646px;height:265px;
    background:linear-gradient(110deg,#3e64b2 0%,#2d58ad 45%,#4a6fb8 75%,#2b55a8 100%)}
  .cap-text{left:34px;top:64px;color:#fff;width:560px}
  .cap-kicker{font-weight:500;font-size:14px;line-height:18px}
  .cap-title{font-weight:800;font-size:25px;line-height:30px;margin-bottom:8px}
  .cap-body{font-weight:500;font-size:11.4px;line-height:16.5px}

  .detail-col{top:276px}
  .detail-col.eccentrics{left:34px}
  .detail-col.sheller{left:250px}
  .detail-col.deck{left:452px}
  .detail-head{font-weight:700;font-size:16.5px;line-height:22px;text-transform:uppercase;margin-bottom:4px}
  .detail-head.screens{margin-top:8px}
  .detail-list{list-style:none;font-weight:500;font-size:9.8px;line-height:14.5px}
  .detail-list li{padding-left:16px}
  .detail-list li::before{width:8px;height:8px;top:3.5px}
  .detail-list li::after{left:2.3px;top:5.3px;width:3.4px;height:2px;border-width:1.2px}

  .grid-tile{width:120px;height:110px;border:3px solid var(--brand-tan)}
  .g1{left:36px;top:525px;background:linear-gradient(150deg,#7d7467,#c6c0b5 55%,#8a8175)}
  .g2{left:168px;top:525px;background:linear-gradient(160deg,#a7a49e,#7a7873 50%,#cfccc5)}
  .g3{left:298px;top:525px;background:linear-gradient(135deg,#a09a90,#d2cdc3 50%,#8d877d)}
  .g4{left:36px;top:645px;background:linear-gradient(160deg,#9c7355,#d5b291 50%,#7f5c44)}
  .g5{left:168px;top:645px;background:linear-gradient(150deg,#8e8c86,#c4c1ba 50%,#5f5d59)}
  .g6{left:298px;top:645px;background:linear-gradient(135deg,#bca27a,#dbc59f 50%,#a88c62)}
  .tall-photo{left:452px;top:398px;width:166px;height:359px;border:3px solid var(--brand-tan);
    background:linear-gradient(180deg,#b3a58e 0%,#d9d6cf 35%,#a7a39b 70%,#8f7f66 100%)}

  .partner-row{left:34px;top:770px;width:584px;height:38px;display:flex;align-items:center}
  .partner{flex:1;font-weight:600;font-size:13px;color:#8a8a8a;text-align:center;line-height:1}
  .partner:first-child{text-align:left;flex:0 0 136px}
  .partner+.partner{border-left:1.5px solid var(--brand-blue);height:34px;display:flex;align-items:center;justify-content:center}
</style>
</head>
<body>

<!-- Front side -->
<main class="sheet front">
  <div class="abs brand">TOVRIX</div>

  <div class="abs hero-band" role="img" aria-label="Blue-tinted view of a peanut processing floor"></div>
  <div class="abs hero-text">
    <p class="hero-kicker">We Manufacture &amp; Supply</p>
    <h1 class="hero-title">Replacement<br>parts for<br><span class="accent">Peanut<br>Processing</span><br>Equipment</h1>
  </div>

  <svg class="abs hero-photo" viewBox="0 0 301 330" role="img" aria-label="Close-up of shelled peanuts moving along a processing conveyor">
    <defs>
      <linearGradient id="peanutTones" x1="0" y1="0" x2="0.4" y2="1">
        <stop offset="0" stop-color="#6f6f72"/>
        <stop offset="0.35" stop-color="#c58a4c"/>
        <stop offset="0.75" stop-color="#a86a35"/>
        <stop offset="1" stop-color="#7c818b"/>
      </linearGradient>
    </defs>
    <path d="M6,24 Q150,-2 295,24 L295,200 Q295,282 150,324 Q6,282 6,200 Z" fill="url(#peanutTones)" stroke="#fff" stroke-width="6"/>
  </svg>

  <section class="abs intro">
    <p class="lead">We believe in simple small town values like hard work,<br>community and quality. That’s why you’ll find our team<br>working day in and day out to provide our customers with quality products.</p>
    <p class="detail">Our replacement parts are designed and manufactured in our fabrication facility in Marlow, AL. With our American made parts, you can be assured of quality, availability and on-time delivery. Our parts are fabricated to exact customer specifications.</p>
  </section>

  <h2 class="abs section-head categories">Product category :</h2>
  <div class="abs category-band">
    <ul class="category-col tick-list">
      <li>Flat Screens</li>
      <li>Sheller Grates</li>
      <li>Ripple Screens</li>
      <li>Sheller Bars</li>
      <li class="wrap">Eccentric Bearing<br>Housings</li>
    </ul>
    <ul class="category-col tick-list">
      <li>Eccentric Shafts</li>
      <li>Rebuilt Machines</li>
      <li>Ducts</li>
      <li>Sprockets</li>
    </ul>
    <ul class="category-col tick-list">
      <li>Rubber Gum Balls</li>
      <li>Fiberglass</li>
      <li>Mellin Pike Reels</li>
      <li>Elevator Buckets</li>
    </ul>
  </div>

  <h2 class="abs section-head products">Several product :</h2>
  <div class="abs product-row">
    <div class="product-tile tile-screens" role="img" aria-label="Stacked ripple screens"></div>
    <div class="product-tile tile-housing" role="img" aria-label="Eccentric bearing housing"></div>
    <div class="product-tile tile-shafts" role="img" aria-label="Steel eccentric shafts"></div>
    <div class="product-tile tile-reels" role="img" aria-label="Wire reel screens"></div>
  </div>

  <svg class="abs footer" viewBox="0 0 646 73" preserveAspectRatio="none" aria-hidden="true">
    <rect x="0" y="36" width="646" height="37" fill="var(--brand-tan)"/>
    <polygon points="0,0 316,0 346,73 0,73" fill="var(--brand-blue)"/>
  </svg>
  <div class="abs location">
    <svg width="18" height="22" viewBox="0 0 20 24" aria-hidden="true">
      <path d="M10 2a6.5 6.5 0 0 0-6.5 6.5C3.5 13 10 19 10 19s6.5-6 6.5-10.5A6.5 6.5 0 0 0 10 2z" fill="none" stroke="#fff" stroke-width="2"/>
      <circle cx="10" cy="8.5" r="2.3" fill="#fff"/>
      <ellipse cx="10" cy="21" rx="7" ry="2" fill="none" stroke="#fff" stroke-width="1.5"/>
    </svg>
    <div>
      <div class="location-label">Location</div>
      <div class="location-address">412 W Foundry Lane Marlow, AL 36301</div>
    </div>
  </div>
  <div class="abs contact">
    <div class="contact-name">Dana Merrow</div>
    <div class="contact-email">
      <svg width="13" height="10" viewBox="0 0 15 11" aria-hidden="true"><rect x="0.5" y="0.5" width="14" height="10" fill="var(--ink)"/><path d="M1 1l6.5 5L14 1" fill="none" stroke="#fff" stroke-width="1.2"/></svg>
      Email : dana@tovrixinc.com
    </div>
    <div class="contact-phone">
      <svg width="16" height="16" viewBox="0 0 24 24" aria-hidden="true"><path d="M6.6 10.8a15 15 0 0 0 6.6 6.6l2.2-2.2a1 1 0 0 1 1-.25 11.4 11.4 0 0 0 3.6.57 1 1 0 0 1 1 1V20a1 1 0 0 1-1 1A17 17 0 0 1 3 4a1 1 0 0 1 1-1h3.5a1 1 0 0 1 1 1c0 1.25.2 2.45.57 3.570a1 1 0 0 1-.25 1z" fill="var(--ink)"/></svg>
      (334) 555-0187
    </div>
  </div>
</main>

<!-- Back side -->
<section class="sheet back">
  <div class="abs cap-band" role="img" aria-label="Blue-tinted photo of a worker on the fabrication floor"></div>
  <div class="abs cap-text">
    <p class="cap-kicker">OUR CAPABILITIES</p>
    <h2 class="cap-title">WHAT WE DO</h2>
    <p class="cap-body">At TOVRIX, Inc., we manufacture and distribute replacement parts for peanut<br>processing equipment. American-made, high-quality parts that are designed to work<br>great in your equipment. We have been producing, reliable products at our facility<br>Marlow, Alabama since 1996.</p>
  </div>

  <div class="abs detail-col eccentrics">
    <h3 class="detail-head">Eccentrics</h3>
    <ul class="detail-list tick-list">
      <li>Eccentric Bearings</li>
      <li>Eccentric Cams</li>
      <li>Eccentric Housings</li>
      <li>Eccentric Rods</li>
      <li>Support Springs &amp; Connectors</li>
      <li>Phenolic Pads</li>
      <li>Drive Guards</li>
      <li>Ducts (Curtains for Separators,</li>
      <li>Stoners &amp; Shakers)</li>
      <li>Shafting</li>
      <li>Elevator Chains</li>
      <li>Sprockets</li>
      <li>Brevik Clamps</li>
      <li>Gum Rubber Balls</li>
    </ul>
  </div>

  <div class="abs detail-col sheller">
    <h3 class="detail-head">Sheller Parts</h3>
    <ul class="detail-list tick-list">
      <li>Corlan Sheller Grates</li>
      <li>Sheller Bars (Lead, Return,<br>and Nub)</li>
      <li>Sheller Hopper Boxes</li>
    </ul>
    <h3 class="detail-head screens">Screens</h3>
    <ul class="detail-list tick-list">
      <li>Rippled Screens (Low &amp; High<br>Profile for Separator and<br>Stoner Decks)</li>
      <li>Perforated Flat Screens<br>(Round and Slotted)</li>
      <li>Screen Frames</li>
      <li>Air Intake Filter Screens</li>
    </ul>
  </div>

  <div class="abs detail-col deck">
    <h3 class="detail-head">Deck Parts</h3>
    <ul class="detail-list tick-list">
      <li>Deck Cap Assemblies and<br>Components</li>
      <li>Food Grade Deck Sealant<br>(Weather Stripping)</li>
      <li>Misc Deck Components</li>
    </ul>
  </div>

  <div class="abs grid-tile g1" role="img" aria-label="Racks of stored screen sheets"></div>
  <div class="abs grid-tile g2" role="img" aria-label="Rippled screen close-up"></div>
  <div class="abs grid-tile g3" role="img" aria-label="Rolled wire screens"></div>
  <div class="abs grid-tile g4" role="img" aria-label="Elevator buckets in a row"></div>
  <div class="abs grid-tile g5" role="img" aria-label="Machined eccentric hub"></div>
  <div class="abs grid-tile g6" role="img" aria-label="Large sprocket gear"></div>
  <div class="abs tall-photo" role="img" aria-label="Worker pressure-washing equipment outdoors"></div>

  <div class="abs partner-row">
    <div class="partner">Corlan</div>
    <div class="partner">Brevik</div>
    <div class="partner">Northway Industries</div>
    <div class="partner">Mellin Pike</div>
  </div>

  <svg class="abs footer" viewBox="0 0 646 73" preserveAspectRatio="none" aria-hidden="true">
    <rect x="0" y="36" width="646" height="37" fill="var(--brand-tan)"/>
    <polygon points="0,0 323,0 358,73 0,73" fill="var(--brand-blue)"/>
  </svg>
  <div class="abs location">
    <div>
      <div class="location-label">Location</div>
      <div class="location-address">412 W Foundry Lane Marlow, AL 36301</div>
    </div>
  </div>
  <div class="abs contact">
    <div class="contact-name">Dana Merrow</div>
    <div class="contact-email">
      <svg width="13" height="10" viewBox="0 0 15 11" aria-hidden="true"><rect x="0.5" y="0.5" width="14" height="10" fill="var(--ink)"/><path d="M1 1l6.5 5L14 1" fill="none" stroke="#fff" stroke-width="1.2"/></svg>
      Email : dana@tovrixinc.com
    </div>
    <div class="contact-phone">
      <svg width="16" height="16" viewBox="0 0 24 24" aria-hidden="true"><path d="M6.6 10.8a15 15 0 0 0 6.6 6.6l2.2-2.2a1 1 0 0 1 1-.25 11.4 11.4 0 0 0 3.6.57 1 1 0 0 1 1 1V20a1 1 0 0 1-1 1A17 17 0 0 1 3 4a1 1 0 0 1 1-1h3.5a1 1 0 0 1 1 1c0 1.25.2 2.45.57 3.57a1 1 0 0 1-.25 1z" fill="var(--ink)"/></svg>
      (334) 555-0187
    </div>
  </div>
</section>

</body>
</html>
```